Business cards for Remote DBA team

Business cards for team offering database administration, consultation, machine learning and AI services. As of now team is using both
www.korvilnet.cz and www.brestmoorlab.cz URLs

Target Market(s)

IT managers

Industry/Entity Type

It Professional

Contact Information for Business Card

Should include logo
name, email, phone, twitter tag

Font styles to use
Sans Serif

Colors

Designer to choose colors to be used in the design.

```html
<!DOCTYPE html>
<html lang="en">
<head>
<meta charset="utf-8">
<title>Korvil Lab – Business Cards</title>
<link href="https://fonts.googleapis.com/css2?family=Montserrat:wght@400;500;800&display=swap" rel="stylesheet">
<style>
  :root {
    --page-bg: #d9dadc;
    --card-white: #f4f4f4;
    --brand-blue: #1479b8;
    --accent-cyan: #1ea3d6;
    --ink: #1d1d1f;
    --rule-grey: #8a8a8a;
    --grad-top: #4b2fa6;
    --grad-mid: #2a63c4;
    --grad-bottom: #1cb3dc;
    --white: #ffffff;
  }
  * { margin: 0; padding: 0; box-sizing: border-box; }
  html, body { width: 1200px; height: 1021px; overflow: hidden; }
  body {
    background: var(--page-bg);
    font-family: "Montserrat", sans-serif;
    display: flex;
    flex-direction: column;
    align-items: center;
    justify-content: center;
    gap: 22px;
  }
  .card {
    width: 840px;
    height: 480px;
    position: relative;
    box-shadow: 0 6px 18px rgba(0,0,0,.18);
  }
  /* Front */
  .card--front {
    overflow: hidden;
  }
  .front-art {
    position: absolute; inset: 0;
    background:
      radial-gradient(circle at 52% 58%, rgba(60,190,235,.35) 0 28%, transparent 46%),
      linear-gradient(180deg, var(--grad-top) 0%, var(--grad-mid) 48%, var(--grad-bottom) 100%);
  }
  .front-logo {
    position: absolute;
    left: 50%; top: 50%;
    transform: translate(-50%, -50%);
    display: flex; align-items: center; gap: 18px;
  }
  .brand-name {
    font-weight: 800;
    letter-spacing: .5px;
    line-height: .95;
    text-transform: uppercase;
  }
  .front-logo .brand-name { color: var(--white); font-size: 64px; }
  .brand-dot {
    width: 26px; height: 26px; border-radius: 50%;
  }
  .front-logo .brand-dot { background: var(--white); }

  /* Back */
  .card--back {
    background: var(--card-white);
    display: flex;
    align-items: center;
  }
  .back-logo {
    width: 430px;
    display: flex; align-items: center; justify-content: center; gap: 14px;
  }
  .back-logo .brand-name { color: var(--brand-blue); font-size: 52px; }
  .back-logo .brand-dot { background: var(--brand-blue); width: 22px; height: 22px; }
  .divider {
    width: 2px; height: 220px; background: var(--rule-grey);
  }
  .contact {
    padding-left: 48px;
    color: var(--ink);
  }
  .person-name {
    color: var(--accent-cyan);
    font-weight: 500;
    font-size: 27px;
    letter-spacing: .5px;
  }
  .person-role {
    font-size: 20px;
    margin-top: 2px;
    margin-bottom: 30px;
  }
  .contact-list { list-style: none; }
  .contact-list li {
    display: flex; align-items: center; gap: 10px;
    font-size: 23px; line-height: 1.2;
    letter-spacing: .3px;
  }
  .contact-list svg { width: 18px; height: 18px; flex: none; }
  .social-dot {
    width: 18px; height: 18px; border-radius: 50%;
    background: var(--accent-cyan); flex: none;
  }
</style>
</head>
<body>

<section class="card card--front">
  <div class="front-art" role="img" aria-label="Purple to cyan gradient background with circuit-line and world-map texture"></div>
  <div class="front-logo">
    <span class="brand-dot"></span>
    <span class="brand-name">Korvil<br>Lab</span>
  </div>
</section>

<section class="card card--back">
  <div class="back-logo">
    <span class="brand-dot"></span>
    <span class="brand-name">Korvil<br>Lab</span>
  </div>
  <div class="divider"></div>
  <div class="contact">
    <p class="person-name">Tomas Varga</p>
    <p class="person-role">Data Platform Architect</p>
    <ul class="contact-list">
      <li>
        <svg viewBox="0 0 24 24" aria-hidden="true"><path fill="var(--accent-cyan)" d="M6.6 10.8a15.1 15.1 0 0 0 6.6 6.6l2.2-2.2c.3-.3.7-.4 1-.2 1.1.4 2.3.6 3.6.6.6 0 1 .4 1 1V20c0 .6-.4 1-1 1C10.6 21 3 13.4 3 4c0-.6.4-1 1-1h3.5c.6 0 1 .4 1 1 0 1.3.2 2.5.6 3.6.1.3 0 .7-.2 1z"/></svg>
        (555) 014-2287
      </li>
      <li>
        <svg viewBox="0 0 24 24" aria-hidden="true"><rect x="2" y="5" width="20" height="14" fill="none" stroke="var(--accent-cyan)" stroke-width="2"/><path d="M2 5l10 8 10-8" fill="none" stroke="var(--accent-cyan)" stroke-width="2"/></svg>
        tomas@korvilnet.cz
      </li>
      <li>
        <svg viewBox="0 0 24 24" aria-hidden="true"><g fill="none" stroke="var(--accent-cyan)" stroke-width="2"><circle cx="12" cy="12" r="10"/><ellipse cx="12" cy="12" rx="4" ry="10"/><path d="M2 12h20"/></g></svg>
        www.korvilnet.cz
      </li>
      <li>
        <svg viewBox="0 0 24 24" aria-hidden="true"><g fill="none" stroke="var(--accent-cyan)" stroke-width="2"><circle cx="12" cy="12" r="10"/><ellipse cx="12" cy="12" rx="4" ry="10"/><path d="M2 12h20"/></g></svg>
        www.brestmoorlab.cz
      </li>
      <li>
        <span class="social-dot"></span>
        @korvillab
      </li>
    </ul>
  </div>
</section>

</body>
</html>
```